Flyer for the Radiant Harvest Worship Day

I am looking to create a flyer for a one day prayer retreat our church is organizing.
This flyer will be posted on social media, websites and will also be printed so it can be mailed to people.
I am looking for something professional, with good use of our logo and band colors (logo colors).
I am counting on the designer's skill, creativity, art and knowledge of media communication to produce a flyer that will effectively and quickly convey the message we are trying to spread.
CONTENT OF THE FLYER:
Event title: Radiant Harvest Worship Day
Date: Tuesday July 2nd, 2019
Time: 11:00AM - 7:00PM
Belmont Hotel, 4875 Maple Ridge Road, Portland, Maine 04219 (Room: Evergreen)
Event Key words to highlight what the event is about: Prayer, Sharing the Word, Panel discussion, prophecy, Impartation.
Key phrases:
A one day prayer retreat.
Jesus Chris is Lord
Contact info:
www.tuvela.org
Phone: 207 583 2194
Email: contact@brookmeadow.org

```html
<!DOCTYPE html>
<html lang="en">
<head>
<meta charset="utf-8">
<title>Radiant Harvest Worship Day</title>
<link href="https://fonts.googleapis.com/css2?family=Yeseva+One&family=Poppins:wght@500;600;700&family=Cinzel:wght@500&display=swap" rel="stylesheet">
<style>
  :root {
    --backdrop: #6b6b6b;
    --night: #070707;
    --sky-rose: #e9b6a4;
    --sky-peach: #f6d3ae;
    --sun: #fff3d6;
    --ember: #e38a2e;
    --navy: #133359;
    --copper: #e0a068;
    --copper-bar: #c98a55;
    --white: #ffffff;
  }
  * { margin: 0; padding: 0; box-sizing: border-box; }
  html, body { width: 1141px; height: 1200px; overflow: hidden; }
  body { background: var(--backdrop); position: relative; }

  .flyer {
    position: absolute;
    left: 222px; top: 62px;
    width: 708px; height: 1000px;
    overflow: hidden;
    background: var(--night);
    color: var(--white);
    font-family: "Poppins", sans-serif;
  }
  .hero-photo {
    position: absolute; inset: 0;
    background:
      linear-gradient(90deg, var(--night) 0%, rgba(7,7,7,0.95) 45%, rgba(7,7,7,0.55) 62%, rgba(7,7,7,0) 80%),
      linear-gradient(180deg, rgba(7,7,7,0) 55%, rgba(7,7,7,0.85) 82%, var(--night) 100%),
      radial-gradient(ellipse 280px 200px at 85% 48%, var(--sun) 0%, rgba(255,230,170,0.6) 40%, rgba(255,220,160,0) 100%),
      linear-gradient(180deg, var(--sky-rose) 0%, var(--sky-peach) 35%, #f3c07a 55%, var(--ember) 68%, #6b3a12 85%);
  }
  .brand-block {
    position: absolute;
    left: 481px; top: 0;
    width: 158px; height: 154px;
    background: var(--navy);
    display: flex; align-items: center; justify-content: center;
  }
  .brand-name {
    font-family: "Cinzel", serif;
    font-weight: 500;
    font-size: 30px;
    letter-spacing: 1px;
    color: var(--white);
  }
  .event-title {
    position: absolute;
    left: 72px; top: 298px;
    font-family: "Yeseva One", serif;
    font-weight: 400;
    font-size: 74px;
    line-height: 76px;
    color: var(--white);
  }
  .highlights {
    position: absolute;
    left: 72px; top: 667px;
    list-style: none;
    font-weight: 600;
    font-size: 18px;
    line-height: 29px;
    color: var(--copper);
  }
  .schedule {
    position: absolute;
    left: 72px; top: 850px;
    font-weight: 600;
    font-size: 17px;
    color: var(--white);
  }
  .schedule .divider { margin: 0 6px; }
  .venue, .contact {
    position: absolute;
    font-weight: 700;
    font-size: 12px;
    line-height: 14.5px;
    color: var(--white);
  }
  .venue { left: 72px; top: 921px; }
  .contact { left: 442px; top: 935px; }
  .web-bar {
    position: absolute;
    left: 72px; top: 977px;
    width: 267px; height: 23px;
    background: var(--copper-bar);
    color: var(--night);
    font-weight: 700; font-size: 12px;
    display: flex; align-items: center; justify-content: center;
  }
</style>
</head>
<body>
  <main class="flyer">
    <div class="hero-photo" role="img" aria-label="Photo area: warm sunset sky with a dark worshipful silhouette fading into black"></div>

    <div class="brand-block"><span class="brand-name">TUVELA</span></div>

    <h1 class="event-title">Radiant<br>Harvest<br>Worship<br>Day</h1>

    <ul class="highlights">
      <li>Prayer</li>
      <li>Sharing the Word</li>
      <li>Panel Discussion</li>
      <li>Prophecy</li>
      <li>Impartation.</li>
    </ul>

    <p class="schedule">Date: Tuesday July 2nd, 2019<span class="divider">|</span>Time: 11:00AM - 7:00PM</p>
    <p class="venue">Venue:<br>Belmont Hotel, 4875 Maple Ridge Road,<br>Portland, Maine 04219 (Room: Evergreen)</p>
    <p class="contact">Phone: 207 583 2194<br>Email: contact@brookmeadow.org</p>
    <div class="web-bar">www.tuvela.org</div>
  </main>
</body>
</html>
```